Business Card Design with new logo

Dorian Pelleway 4172
E 118th St Halby, IL 62907
Cell: 217-555-0193
pellewayrestoration@mailvane.test

Classic Car Restoration Services Buy Sell Trade Consign

Dorian Pelleway 9698
Cell: 217-555-0193

```html
<!DOCTYPE html>
<html lang="en">
<head>
<meta charset="utf-8">
<title>Pelleway Restoration LLC – Business Card</title>
<link rel="stylesheet" href="https://fonts.googleapis.com/css2?family=Oswald:wght@500&family=Exo+2:ital,wght@1,700&family=Lato:wght@400;700&display=swap">
<style>
  :root {
    --bg: #ececec;
    --red-deep: #b81f24;
    --red-bright: #e8322e;
    --navy: #1c2633;
    --ink: #1a1a1a;
    --paper: #ffffff;
    --muted: #3a3a3a;
  }
  * { margin: 0; padding: 0; box-sizing: border-box; }
  html, body { width: 1200px; height: 586px; overflow: hidden; }
  body { background: var(--bg); position: relative; font-family: "Lato", sans-serif; }

  .card {
    position: absolute;
    top: 128px;
    width: 502px;
    height: 300px;
    overflow: hidden;
  }

  /* Front */
  .card-front { left: 61px; background: var(--red-deep); color: var(--paper); }
  .front-brand {
    position: absolute;
    left: 44px;
    top: 218px;
    width: 200px;
    text-align: center;
    font-family: "Oswald", sans-serif;
    font-weight: 500;
    color: var(--paper);
    white-space: nowrap;
  }
  .front-brand .brand-name { font-size: 26px; letter-spacing: 10px; margin-right: -10px; line-height: 1; }
  .front-brand .brand-sub { font-size: 10px; letter-spacing: 7.5px; margin-right: -7.5px; margin-top: 5px; line-height: 1; }
  .tagline {
    position: absolute;
    left: 44px;
    top: 266px;
    font-family: "Exo 2", sans-serif;
    font-style: italic;
    font-weight: 700;
    font-size: 11.5px;
  }

  /* Back */
  .card-back { left: 619px; background: var(--paper); }
  .back-brand {
    position: absolute;
    left: 0; right: 0;
    top: 97px;
    text-align: center;
    font-family: "Oswald", sans-serif;
    font-weight: 500;
    color: var(--navy);
    white-space: nowrap;
  }
  .back-brand .brand-name { font-size: 30px; letter-spacing: 12px; margin-right: -12px; line-height: 1; }
  .back-brand .brand-sub { font-size: 10px; letter-spacing: 8.5px; margin-right: -8.5px; margin-top: 6px; line-height: 1; color: var(--red-deep); }

  .person {
    position: absolute;
    right: 286px;
    top: 196px;
    text-align: right;
  }
  .person-name {
    font-family: "Oswald", sans-serif;
    font-weight: 500;
    font-size: 15px;
    color: var(--red-deep);
    letter-spacing: 0.5px;
    line-height: 1.1;
  }
  .person-role { font-size: 10.5px; color: var(--muted); margin-top: 2px; }
  .person-address { font-size: 11.5px; font-weight: 700; color: var(--red-deep); margin-top: 10px; white-space: nowrap; }

  .divider {
    position: absolute;
    left: 240px;
    top: 186px;
    width: 2px;
    height: 78px;
    background: linear-gradient(to bottom, transparent, var(--red-bright), transparent);
  }
  .contact { position: absolute; left: 266px; top: 204px; list-style: none; }
  .contact li { display: flex; align-items: center; gap: 8px; font-size: 11.5px; color: var(--ink); height: 24px; white-space: nowrap; }
  .contact svg { width: 16px; height: 16px; flex: none; }

  .band { position: absolute; bottom: 0; height: 10px; }
  .band-left { left: 0; width: 251px; background: var(--red-bright); }
  .band-right { left: 251px; right: 0; background: var(--red-deep); }
</style>
</head>
<body>

<section class="card card-front" aria-label="Card front">
  <div class="front-brand">
    <div class="brand-name">PELLEWAY</div>
    <div class="brand-sub">RESTORATION LLC</div>
  </div>
  <p class="tagline">Classic Car Restoration Services Buy Sell Trade Consign</p>
</section>

<section class="card card-back" aria-label="Card back">
  <div class="back-brand">
    <div class="brand-name">PELLEWAY</div>
    <div class="brand-sub">RESTORATION LLC</div>
  </div>

  <div class="person">
    <div class="person-name">DORIAN PELLEWAY</div>
    <div class="person-role">Marlow Advisors</div>
    <div class="person-address">4172 E 118th St Halby, IL 62907</div>
  </div>

  <div class="divider"></div>

  <ul class="contact">
    <li>
      <svg viewBox="0 0 16 16" aria-hidden="true"><circle cx="8" cy="8" r="8" fill="var(--red-deep)"/><path d="M4.5 6.5c0-1 1.5-1.8 3.5-1.8s3.5.8 3.5 1.8v.6H9.8v-.7H6.2v.7H4.5z M5.5 8h5l.7 3.3H4.8z" fill="#fff"/></svg>
      217-555-0193
    </li>
    <li>
      <svg viewBox="0 0 16 16" aria-hidden="true"><circle cx="8" cy="8" r="8" fill="var(--red-deep)"/><rect x="4.2" y="5.3" width="7.6" height="5.4" fill="#fff"/><path d="M4.2 5.3 8 8.3l3.8-3" fill="none" stroke="var(--red-deep)" stroke-width="0.9"/></svg>
      pellewayrestoration@mailvane.test
    </li>
  </ul>

  <div class="band band-left"></div>
  <div class="band band-right"></div>
</section>

</body>
</html>
```